Larkspur Stillness

Logo picture and I want it to say

yoga. meditation. sound healing

small sweet classes

Larkspur-stillness.com

2740 West Hollander Ave Suite K
Santa Barbara ca 93108

```html
<!DOCTYPE html>
<html lang="en">
<head>
<meta charset="utf-8">
<title>Larkspur Stillness Flyer</title>
<link rel="stylesheet" href="https://fonts.googleapis.com/css2?family=Questrial&family=Open+Sans:wght@400;600;700&display=swap">
<style>
  :root {
    --navy: #3b3f72;
    --violet: #8a7bbf;
    --white: #ffffff;
    --ink: #3a3a4a;
    --photo-light: #e9e4e0;
    --photo-mid: #c9bdb4;
  }
  * { margin: 0; padding: 0; box-sizing: border-box; }
  html, body { width: 1041px; height: 1200px; overflow: hidden; background: #fff; }
  .flyer {
    position: relative;
    width: 1041px;
    height: 1200px;
    overflow: hidden;
    font-family: "Open Sans", sans-serif;
    color: var(--white);
  }
  .hero-photo {
    position: absolute;
    inset: 0 0 auto 0;
    height: 700px;
    background: linear-gradient(160deg, var(--photo-light) 0%, var(--photo-mid) 55%, #a89a94 100%);
  }
  .shapes { position: absolute; inset: 0; width: 1041px; height: 1200px; }
  .brand-mark {
    position: absolute;
    left: 729px; top: 510px;
    width: 250px; height: 250px;
    border: 3px solid var(--white);
    border-radius: 50%;
    display: flex; align-items: center; justify-content: center;
    text-align: center;
    font-family: "Questrial", sans-serif;
    font-size: 30px;
    line-height: 1.15;
    color: var(--white);
  }
  .tagline {
    position: absolute;
    top: 772px; left: 0; width: 100%;
    text-align: center;
    font-family: "Questrial", sans-serif;
    font-weight: 400;
    font-size: 54px;
    letter-spacing: 0.3px;
  }
  .subline {
    position: absolute;
    top: 850px; left: 0; width: 100%;
    text-align: center;
    font-weight: 600;
    font-size: 36px;
    letter-spacing: 0.5px;
  }
  .web-pill {
    position: absolute;
    top: 917px; left: 226px;
    width: 580px; height: 44px;
    border-radius: 22px;
    background: var(--navy);
    display: flex; align-items: center; justify-content: center; gap: 14px;
    font-weight: 600;
    font-size: 28px;
  }
  .address {
    position: absolute;
    top: 988px; left: 0; width: 100%;
    text-align: center;
    font-size: 23px;
    line-height: 30px;
  }
  .contact {
    position: absolute;
    right: 36px; top: 1100px;
    text-align: right;
    color: var(--ink);
    font-size: 20px;
    line-height: 30px;
  }
  .contact li { list-style: none; display: flex; justify-content: flex-end; align-items: center; gap: 10px; }
  .contact svg { width: 20px; height: 20px; }
</style>
</head>
<body>
<main class="flyer">
  <div class="hero-photo" role="img" aria-label="Photo of a group of people seated cross-legged, meditating in a bright studio"></div>

  <svg class="shapes" viewBox="0 0 1041 1200" preserveAspectRatio="none" aria-hidden="true">
    <defs>
      <linearGradient id="panelGradient" x1="0" y1="0" x2="1" y2="1">
        <stop offset="0" stop-color="#b07fb8"/>
        <stop offset="0.45" stop-color="#8a7bbf"/>
        <stop offset="0.8" stop-color="#7d8ccc"/>
        <stop offset="1" stop-color="#8b6fb3"/>
      </linearGradient>
    </defs>
    <path class="corner-blob" d="M0,0 L320,0 C300,30 260,50 200,56 C130,62 70,90 0,140 Z" fill="#7b74b4"/>
    <path class="corner-blob-dark" d="M0,0 L200,0 C170,24 120,40 70,52 C40,60 20,70 0,80 Z" fill="var(--navy)"/>
    <path class="wave-band" d="M0,586 C200,640 420,610 620,500 S930,385 1041,372 L1041,1200 L0,1200 Z" fill="var(--navy)"/>
    <path class="wave-panel" d="M0,668 C250,700 480,660 680,540 S960,405 1041,392 L1041,1200 L0,1200 Z" fill="url(#panelGradient)"/>
    <path class="corner-rim" d="M460,1200 Q560,1045 1041,1040 L1041,1200 Z" fill="var(--navy)"/>
    <path class="corner-card" d="M500,1200 Q600,1080 1041,1058 L1041,1200 Z" fill="var(--white)"/>
  </svg>

  <div class="brand-mark">Larkspur<br>Stillness</div>

  <h1 class="tagline">Yoga. Meditation. Sound Healing</h1>
  <p class="subline">SMALL SWEET CLASSES</p>

  <div class="web-pill">
    <svg width="22" height="22" viewBox="0 0 22 22" aria-hidden="true">
      <circle cx="11" cy="11" r="9" fill="none" stroke="#fff" stroke-width="1.8"/>
      <ellipse cx="11" cy="11" rx="4" ry="9" fill="none" stroke="#fff" stroke-width="1.4"/>
      <line x1="2" y1="11" x2="20" y2="11" stroke="#fff" stroke-width="1.4"/>
    </svg>
    <span>larkspur-stillness.com</span>
  </div>

  <p class="address">2740 West Hollander Ave Suite K Santa Barbara Ca 93108<br>larkspur-stillness.com for more details</p>

  <ul class="contact">
    <li>(805) 555-0142
      <svg viewBox="0 0 22 22" aria-hidden="true"><circle cx="11" cy="11" r="10" fill="var(--navy)"/><path d="M8 6 L10 8 L9 10 C10 12 11 13 12 13 L14 12 L16 14 L14 16 C10 16 6 12 6 8 Z" fill="#fff"/></svg>
    </li>
    <li>larkspurstillness@mailbox.com
      <svg viewBox="0 0 22 22" aria-hidden="true"><circle cx="11" cy="11" r="10" fill="var(--navy)"/><rect x="6" y="7.5" width="10" height="7" fill="none" stroke="#fff" stroke-width="1.4"/><path d="M6 7.5 L11 11.5 L16 7.5" fill="none" stroke="#fff" stroke-width="1.4"/></svg>
    </li>
    <li>www.larkspur-stillness.com
      <svg viewBox="0 0 22 22" aria-hidden="true"><circle cx="11" cy="11" r="10" fill="var(--navy)"/><circle cx="11" cy="11" r="6" fill="none" stroke="#fff" stroke-width="1.3"/><ellipse cx="11" cy="11" rx="2.6" ry="6" fill="none" stroke="#fff" stroke-width="1.1"/><line x1="5" y1="11" x2="17" y2="11" stroke="#fff" stroke-width="1.1"/></svg>
    </li>
  </ul>
</main>
</body>
</html>
```